Brinevale Yacht Management Full Page Ad Flyer

Yacht Management Package also includes the following periodic Monthly services:

Monthly full vessel systems checklist inspections
Diver For Hull Cleaning And Inspection Of Props, Shafts, and Zincs
Interior/Exterior Detailing and scheduled washdowns
Manage Haulout
Pump-out Services
On-call Captain and Crew Services
Updates

Need more time to provide more content to designers and the printing press template file.

Target Market(s)

Vessel owners, motor yachts, sailboats from 25 feet in length up to 125 feet in length. We do not do cruise ships or yachts larger than 125 feet. Someone who has their boat docked at their house or a local marina. We also offer mobile on-site services.

```html
<!DOCTYPE html>
<html lang="en">
<head>
<meta charset="UTF-8">
<title>Brinevale Yacht Management – Packages</title>
<link href="https://fonts.googleapis.com/css2?family=Poppins:wght@400;500;600;700;800&family=Great+Vibes&display=swap" rel="stylesheet">
<style>
  :root {
    --navy: #1a4f8f;
    --deep: #184f9e;
    --sea: #1f66b5;
    --band-light: #5cc2ee;
    --band-main: #22a5df;
    --footer: #1a5fae;
    --white: #ffffff;
    --ink: #1d3f74;
  }
  * { margin: 0; padding: 0; box-sizing: border-box; }
  html, body { width: 848px; height: 1200px; overflow: hidden; background: var(--white); }
  .flyer {
    position: relative;
    width: 848px;
    height: 1200px;
    overflow: hidden;
    font-family: "Poppins", Arial, sans-serif;
    color: var(--white);
    background: var(--band-main);
  }
  .hero-photo {
    position: absolute;
    left: 0; top: 0;
    width: 848px; height: 780px;
    background: linear-gradient(180deg,
      #f2f5f8 0%, #c9d8e6 12%, #9fb6cc 20%,
      #7d8f52 24%, #5f7a3e 32%, #8a7a4a 38%,
      #2a6ab4 41%, #1f5fae 60%, #1b64b8 100%);
  }
  .waves { position: absolute; left: 0; top: 0; width: 848px; height: 1200px; }

  .brand-tab {
    position: absolute;
    left: 0; top: 0;
    width: 228px; height: 86px;
    background: var(--white);
    border-bottom-right-radius: 60px;
    display: flex; flex-direction: column; align-items: center; justify-content: center;
    padding-right: 18px;
    color: var(--ink);
    font-weight: 500;
  }
  .brand-name { font-size: 21px; letter-spacing: 3px; line-height: 1; }
  .brand-sub { font-size: 8px; letter-spacing: 2.6px; margin-top: 5px; }

  .headline { position: absolute; left: 0; top: 478px; width: 848px; text-align: center; }
  .headline-main {
    font-weight: 800; font-size: 84px; letter-spacing: 2px; line-height: 1;
    padding-left: 20px;
  }
  .headline-script {
    font-family: "Great Vibes", cursive;
    font-size: 112px; line-height: 1; margin-top: -22px; padding-left: 20px;
  }
  .packages-pill {
    display: inline-block;
    margin-top: 0;
    padding: 6px 26px 4px;
    background: var(--white);
    color: var(--navy);
    border-radius: 10px;
    font-weight: 700; font-size: 34px; letter-spacing: 0.5px;
    box-shadow: 0 4px 8px rgba(0,0,0,.2);
  }

  .services { position: absolute; top: 790px; left: 0; width: 848px; height: 300px; }
  .service {
    position: absolute;
    display: flex; align-items: center;
    font-size: 21px; font-weight: 500; line-height: 1.15;
  }
  .service-icon {
    flex: none;
    width: 46px; height: 46px; border-radius: 50%;
    border: 2px solid var(--white);
    margin-right: 10px;
    display: flex; align-items: center; justify-content: center;
  }
  .connector { position: absolute; width: 2px; background: var(--white); }

  .contact-bar {
    position: absolute; left: 0; top: 1162px; width: 848px; height: 26px;
    font-size: 15px; font-weight: 400;
  }
  .contact { position: absolute; display: flex; align-items: center; gap: 8px; }
  .contact-icon {
    width: 20px; height: 20px; border-radius: 50%; background: var(--white);
    display: flex; align-items: center; justify-content: center;
  }
</style>
</head>
<body>
<div class="flyer">
  <div class="hero-photo" role="img" aria-label="Photograph of a large white motor yacht anchored in a blue bay below green wooded hills under a cloudy sky"></div>

  <svg class="waves" viewBox="0 0 848 1200" aria-hidden="true">
    <path d="M0 735 C120 700 230 755 360 730 C490 705 570 745 690 722 C770 708 815 728 848 720 L848 1200 L0 1200 Z" fill="var(--band-light)"/>
    <path d="M0 770 C140 742 260 792 400 765 C540 738 650 786 848 756 L848 1200 L0 1200 Z" fill="var(--band-main)"/>
    <path d="M0 1118 C150 1092 270 1136 430 1112 C590 1090 710 1130 848 1106 L848 1200 L0 1200 Z" fill="var(--band-light)"/>
    <path d="M0 1132 C160 1110 280 1150 440 1128 C600 1108 720 1144 848 1122 L848 1200 L0 1200 Z" fill="var(--footer)"/>
  </svg>

  <div class="brand-tab">
    <div class="brand-name">BRINEVALE</div>
    <div class="brand-sub">YACHT MANAGEMENT</div>
  </div>

  <div class="headline">
    <div class="headline-main">YACHT</div>
    <div class="headline-script">Management</div>
    <div class="packages-pill">PACKAGES</div>
  </div>

  <div class="services">
    <div class="connector" style="left:53px; top:56px; height:50px;"></div>
    <div class="connector" style="left:53px; top:163px; height:55px;"></div>
    <div class="connector" style="left:459px; top:56px; height:50px;"></div>
    <div class="connector" style="left:459px; top:163px; height:55px;"></div>

    <div class="service" style="left:31px; top:10px;">
      <span class="service-icon"><svg width="22" height="22" viewBox="0 0 22 22"><path d="M5 11 l4 4 l8-9" fill="none" stroke="#fff" stroke-width="2.2" stroke-linecap="round"/></svg></span>
      <span>Monthly full vessel systems<br>checklist inspections</span>
    </div>
    <div class="service" style="left:31px; top:108px;">
      <span class="service-icon"><svg width="22" height="22" viewBox="0 0 22 22"><path d="M5 11 l4 4 l8-9" fill="none" stroke="#fff" stroke-width="2.2" stroke-linecap="round"/></svg></span>
      <span>Diver For Hull Cleaning And<br>Inspection Of Props, Shafts,<br>and Zincs</span>
    </div>
    <div class="service" style="left:31px; top:220px;">
      <span class="service-icon"><svg width="22" height="22" viewBox="0 0 22 22"><path d="M5 11 l4 4 l8-9" fill="none" stroke="#fff" stroke-width="2.2" stroke-linecap="round"/></svg></span>
      <span>Interior/Exterior Detailing<br>and scheduled washdowns</span>
    </div>

    <div class="service" style="left:437px; top:10px;">
      <span class="service-icon"><svg width="22" height="22" viewBox="0 0 22 22"><path d="M5 11 l4 4 l8-9" fill="none" stroke="#fff" stroke-width="2.2" stroke-linecap="round"/></svg></span>
      <span>Manage Haulout</span>
    </div>
    <div class="service" style="left:437px; top:117px;">
      <span class="service-icon"><svg width="22" height="22" viewBox="0 0 22 22"><path d="M5 11 l4 4 l8-9" fill="none" stroke="#fff" stroke-width="2.2" stroke-linecap="round"/></svg></span>
      <span>Pump-out Services</span>
    </div>
    <div class="service" style="left:437px; top:220px;">
      <span class="service-icon"><svg width="22" height="22" viewBox="0 0 22 22"><path d="M5 11 l4 4 l8-9" fill="none" stroke="#fff" stroke-width="2.2" stroke-linecap="round"/></svg></span>
      <span>On-call Captain and Crew<br>Services</span>
    </div>
  </div>

  <div class="contact-bar">
    <div class="contact" style="left:104px;">
      <span class="contact-icon"><svg width="12" height="12" viewBox="0 0 24 24"><path d="M6.6 10.8a15 15 0 0 0 6.6 6.6l2.2-2.2a1 1 0 0 1 1-.25 11.4 11.4 0 0 0 3.6.57 1 1 0 0 1 1 1V20a1 1 0 0 1-1 1A17 17 0 0 1 3 4a1 1 0 0 1 1-1h3.5a1 1 0 0 1 1 1c0 1.25.2 2.45.57 3.6a1 1 0 0 1-.25 1z" fill="var(--footer)"/></svg></span>
      <span>0000-0000000</span>
    </div>
    <div class="contact" style="left:318px;">
      <span class="contact-icon"><svg width="12" height="12" viewBox="0 0 24 24"><rect x="3" y="6" width="18" height="12" rx="1.5" fill="none" stroke="var(--footer)" stroke-width="2.4"/><path d="M3.5 7 l8.5 6 l8.5-6" fill="none" stroke="var(--footer)" stroke-width="2.2"/></svg></span>
      <span>hello@brinevaleyachts.com</span>
    </div>
    <div class="contact" style="left:592px;">
      <span class="contact-icon"><svg width="12" height="12" viewBox="0 0 24 24"><circle cx="12" cy="12" r="9" fill="none" stroke="var(--footer)" stroke-width="2.2"/><ellipse cx="12" cy="12" rx="4" ry="9" fill="none" stroke="var(--footer)" stroke-width="2"/><path d="M3 12h18" stroke="var(--footer)" stroke-width="2"/></svg></span>
      <span>brinevaleyachts.com</span>
    </div>
  </div>
</div>
</body>
</html>
```